Special release wine label

Marrow Creek Vineyards is a small premium wine producer in the Barossa - South Australia. We are a five star rated winery, producing exceptional wines true to variety, region and house style. We have a very special parcel of wine that we wish to release as an exclusive wine. Visit www.marrowcreekvineyards.com.au for further feel.

The wine will be called Marrow Creek Vineyards, 2012, The Quiet Harvest Shiraz - Cabernet.

The wine can be bottled in either a burgundy or Bordeaux shaped bottle

Industry/Entity Type

House

```html
<!DOCTYPE html>
<html lang="en">
<head>
<meta charset="utf-8">
<title>Marrow Creek Vineyards – The Quiet Harvest 2012 Label</title>
<link href="https://fonts.googleapis.com/css2?family=Cinzel:wght@400;700&family=IM+Fell+English+SC&family=Pinyon+Script&display=swap" rel="stylesheet">
<style>
  :root {
    --page: #ffffff;
    --parchment-light: #f3e7d3;
    --parchment: #ead8bd;
    --parchment-edge: #d9c19e;
    --ink-brown: #5a2617;
    --ink-red: #8c1f1c;
    --ink-wine: #6b1513;
    --rule: #6e3322;
    --sketch-light: #e6d3b6;
    --sketch-dark: #a27a5c;
  }
  * { margin: 0; padding: 0; box-sizing: border-box; }
  html, body {
    width: 1200px; height: 948px; overflow: hidden;
    background: var(--page);
  }
  .canvas { position: relative; width: 1200px; height: 948px; }

  .label {
    position: absolute; left: 483px; top: 28px;
    width: 598px; height: 890px;
    background: radial-gradient(ellipse at 50% 45%, var(--parchment-light) 0%, var(--parchment) 70%, var(--parchment-edge) 100%);
    box-shadow: 4px 6px 10px rgba(0,0,0,0.18);
    color: var(--ink-brown);
    text-align: center;
  }
  .label__frame {
    position: absolute; inset: 0;
    border: 3px solid var(--rule);
    pointer-events: none;
  }
  .label__arch { position: absolute; left: 0; top: 28px; width: 598px; height: 80px; overflow: visible; }
  .label__arch text {
    font-family: "Cinzel", serif; font-size: 28px; fill: var(--ink-red);
  }

  .crest {
    position: absolute; left: 128px; top: 92px; width: 342px; height: 60px;
    display: flex; align-items: center; justify-content: center; gap: 12px;
  }
  .crest__flourish {
    width: 80px; height: 26px;
    background: linear-gradient(90deg, transparent, var(--sketch-dark), transparent);
    opacity: 0.55; border-radius: 13px;
  }
  .crest__mark { display: flex; align-items: center; gap: 6px; white-space: nowrap; }
  .crest__dot { width: 10px; height: 10px; border-radius: 50%; background: var(--ink-brown); }
  .crest__name {
    font-family: "Cinzel", serif; font-size: 13px; font-weight: 400;
    color: var(--ink-brown); letter-spacing: 1px; white-space: nowrap;
  }

  .rule { position: absolute; left: 91px; width: 425px; height: 2px; background: var(--rule); }
  .rule--top { top: 160px; }
  .rule--bottom { top: 228px; }

  .estate-name {
    position: absolute; left: 0; right: 0; top: 168px;
    font-family: "Cinzel", serif; font-weight: 700; font-size: 40px;
    letter-spacing: 4px; color: var(--ink-brown); line-height: 52px;
    white-space: nowrap;
  }

  .homestead-sketch {
    position: absolute; left: 111px; top: 252px; width: 375px; height: 265px;
    background: radial-gradient(ellipse at 50% 60%, var(--sketch-light) 0%, #d8bf9c 55%, rgba(216,191,156,0) 80%);
  }

  .estate-word {
    position: absolute; left: 0; right: 0; top: 524px;
    font-family: "Cinzel", serif; font-weight: 700; font-size: 34px;
    letter-spacing: 6px; color: var(--ink-brown); line-height: 44px;
  }
  .wine-title {
    position: absolute; left: 0; right: 0; top: 584px;
    font-family: "IM Fell English SC", serif; font-size: 54px; font-weight: 400;
    color: var(--ink-brown); line-height: 64px;
    white-space: nowrap;
  }
  .vintage {
    position: absolute; left: 0; right: 0; top: 652px;
    font-family: "Cinzel", serif; font-size: 27px; letter-spacing: 2px;
    color: var(--ink-brown); line-height: 34px;
  }
  .varietal {
    position: absolute; left: 0; right: 0; top: 694px;
    font-family: "Pinyon Script", cursive; font-size: 46px;
    color: var(--ink-wine); line-height: 60px; white-space: nowrap;
  }
  .producer-note {
    position: absolute; left: 0; right: 0; top: 780px;
    font-family: "IM Fell English SC", serif; font-size: 13px;
    line-height: 17px; color: var(--ink-brown);
  }
  .volume, .strength {
    position: absolute; top: 808px;
    font-family: "IM Fell English SC", serif; font-size: 24px;
    color: var(--ink-brown); letter-spacing: 1px; white-space: nowrap;
  }
  .volume { left: 16px; }
  .strength { right: 16px; }
  .region {
    position: absolute; left: 0; right: 0; top: 848px;
    font-family: "IM Fell English SC", serif; font-size: 16px;
    letter-spacing: 1px; color: var(--ink-red);
  }
</style>
</head>
<body>
<main class="canvas">
  <section class="label" aria-label="The Quiet Harvest 2012 wine label">
    <svg class="label__arch" viewBox="0 0 598 80" aria-label="Grand Wines of Australia">
      <path id="arch-path" d="M70 72 Q299 10 528 72" fill="none"/>
      <text><textPath href="#arch-path" startOffset="50%" text-anchor="middle" textLength="436" lengthAdjust="spacingAndGlyphs">GRAND WINES OF AUSTRALIA</textPath></text>
    </svg>

    <div class="crest">
      <span class="crest__flourish" role="img" aria-label="Decorative vine scroll"></span>
      <span class="crest__mark">
        <span class="crest__dot"></span>
        <span class="crest__name">MARROW CREEK</span>
      </span>
      <span class="crest__flourish" role="img" aria-label="Decorative vine scroll"></span>
    </div>

    <div class="rule rule--top"></div>
    <h1 class="estate-name">MARROW CREEK</h1>
    <div class="rule rule--bottom"></div>

    <div class="homestead-sketch" role="img" aria-label="Engraved sketch of the vineyard homestead framed by tall palms and a cypress"></div>

    <p class="estate-word">VINEYARDS</p>
    <h2 class="wine-title">The Quiet Harvest</h2>
    <p class="vintage">2012</p>
    <p class="varietal">Shiraz- Cabernet</p>

    <p class="producer-note">
      FROM BEST OUR WINES LIMITED EDITION SPECIAL<br>
      PRODUCT AND BOTTLED BY<br>
      MARROW CREEK VINEYARDS LLC.
    </p>
    <p class="volume">750 ML.</p>
    <p class="strength">13.5% ALK.</p>
    <p class="region">BAROSSA WINERY SOUTH AUSTRALIA</p>

    <div class="label__frame"></div>
  </section>
</main>
</body>
</html>
```